Construction Company - Aluminum Welding Substations - 8 page Brochure

See attached for very rough idea of brochure idea and general idea - primary goal is to highlight various services provided as unique for our industry.

- About Us - see website (brevoforge.com) & Company Resume

- Why Welded Fittings - see PPT & language in comments

- Services Provided - See categories broke out on website - highlight Aluminum Bus Welding, Bus Bending, All Weather Welding, Field Fabrication.

- Contact Page - see website

- Want to use as many photo's to highlight work as possible as people like to see the finished product of the substation/bus bending
Updates

Target Market(s)

General Contractors - we are Specialty Subcontractor

Industry/Entity Type

Construction - Welding Substations

Font styles to use
Serif
Sans Serif

Colors
0054AA
0677BA
7BADD7
CADEEF
E8F1F8
0094D4
00A9DD
6FCCEA
C7EBF8
E9F6FB
F0912C
F2A743
F7CA91
FBE8D2
FDF5EE

Requirements
Must have
• Logo, "Quality Craftsmanship without Compromise", Services Provided, as many pictures as makes sense to highlight work

```html
<!DOCTYPE html>
<html lang="en">
<head>
<meta charset="utf-8">
<title>Brevo Forge – About Us &amp; Services Provided</title>
<link href="https://fonts.googleapis.com/css2?family=Oswald:wght@400;500;700&family=Montserrat:wght@400;600;700&display=swap" rel="stylesheet">
<style>
  :root{
    --bg:#e4e5e7;
    --red:#e8402f;
    --navy:#0f2048;
    --teal:#4db3c6;
    --white:#ffffff;
    --paper:#f4f4f4;
    --ink:#3a3d45;
    --rule:#2a2d35;
  }
  *{box-sizing:border-box;margin:0;padding:0}
  html,body{width:1200px;height:1200px;overflow:hidden;background:var(--bg)}
  body{font-family:"Montserrat",sans-serif;color:var(--ink)}
  .spread{position:absolute;left:60px;top:240px;width:1080px;height:720px;display:flex;box-shadow:0 10px 30px rgba(0,0,0,.18)}
  .panel{position:relative;width:270px;height:720px;overflow:hidden}
  .panel + .panel{border-left:1px solid rgba(0,0,0,.06)}

  /* About spread */
  .about{background:var(--paper)}
  .about-left .red-band{position:absolute;left:0;top:0;width:110px;height:720px;background:var(--red)}
  .about-title{position:absolute;left:12px;top:26px;color:var(--white);font-family:"Oswald",sans-serif;line-height:.85}
  .about-title .small{display:block;font-size:22px;letter-spacing:3px;font-weight:500}
  .about-title .big{display:block;font-size:84px;font-weight:700}
  .about-row{position:absolute;left:0;right:0;border-bottom:1px dashed var(--rule)}
  .about-head{position:absolute;left:122px;width:140px;font-family:"Oswald",sans-serif;font-weight:500;font-size:8.5px;line-height:1.25;color:var(--red);text-transform:uppercase}
  .about-body{position:absolute;left:12px;width:246px;font-size:6.3px;line-height:1.45;color:var(--ink)}
  .about-body b{color:var(--rule)}
  .about-body ul{padding-left:9px}

  .photo{position:absolute;border-radius:6px;background:linear-gradient(160deg,#c9d3dc,#7f8d99 55%,#4c5863)}
  .photo.warm{background:linear-gradient(160deg,#d9dfe4,#a9795b 45%,#5a5f66)}
  .photo.sky{background:linear-gradient(180deg,#9fc3e0,#7e95a8 60%,#57626c)}
  .about-photo{position:absolute;top:430px;height:290px;border-radius:0}
  .about-photo.left{left:110px;width:160px}
  .about-photo.right{left:0;width:270px}
  .fade{position:absolute;left:0;right:0;top:430px;height:120px;background:linear-gradient(var(--paper),rgba(244,244,244,0))}
  .badges{position:absolute;left:12px;top:560px;display:flex;gap:8px;align-items:center}
  .badge{background:var(--white);border:1px solid #c4c8cf}
  .badge.rect{width:52px;height:20px}
  .badge.round{width:26px;height:26px;border-radius:50%}

  /* Services spread */
  .services{background:var(--navy);color:var(--white)}
  .services-left .edge{position:absolute;left:0;top:0;width:8px;height:720px;background:var(--red)}
  .svc-title{position:absolute;left:26px;top:26px;font-family:"Oswald",sans-serif;line-height:.9}
  .svc-title .small{display:block;font-size:16px;letter-spacing:3px;font-weight:400}
  .svc-title .big{display:block;font-size:44px;font-weight:700}
  .svc-sub{position:absolute;left:26px;top:110px;width:200px;font-size:6.3px;line-height:1.45;opacity:.85}
  .dash{position:absolute;left:20px;right:20px;border-top:1px dashed rgba(255,255,255,.55)}

  .card{position:absolute;left:22px;width:178px;border-radius:12px;padding:14px 20px 12px 12px}
  .card .copy{width:138px}
  .card.red{background:var(--red)}
  .card.teal{background:var(--teal)}
  .card .notch{position:absolute;right:-13px;width:26px;height:26px;border-radius:50%;background:var(--navy)}
  .card h3{font-family:"Oswald",sans-serif;font-weight:500;font-size:10px;letter-spacing:.5px;text-transform:uppercase;margin-bottom:4px}
  .card h4{font-family:"Oswald",sans-serif;font-weight:500;font-size:8px;line-height:1.2;text-transform:uppercase;margin:6px 0 2px}
  .card p,.card li{font-size:6.2px;line-height:1.45}
  .card ul{padding-left:9px}
  .pcol .photo{width:72px;height:56px}

  .field-list{position:absolute;left:26px;top:30px;width:220px;font-size:6.6px;line-height:1.5}
  .field-list h5{font-family:"Oswald",sans-serif;font-weight:500;font-size:9px;color:var(--red);text-transform:uppercase;margin-top:5px}
</style>
</head>
<body>
<div class="spread">

  <!-- Panel 1 -->
  <section class="panel about about-left">
    <div class="red-band"></div>
    <h1 class="about-title"><span class="small">ABOUT</span><span class="big">US</span></h1>
    <div class="about-row" style="top:0;height:110px"></div>
    <div class="about-row" style="top:110px;height:80px"></div>
    <div class="about-row" style="top:190px;height:40px"></div>
    <div class="about-row" style="top:230px;height:32px"></div>
    <div class="about-row" style="top:262px;height:40px"></div>
    <div class="about-row" style="top:302px;height:120px"></div>
    <h2 class="about-head" style="top:22px">Family owned business – trusted since incorporation in 1987</h2>
    <h2 class="about-head" style="top:120px">What we believe</h2>
    <h2 class="about-head" style="top:200px">Our team</h2>
    <h2 class="about-head" style="top:240px">Multi-state licensed</h2>
    <h2 class="about-head" style="top:270px">Safety network &amp; contractor registration</h2>
    <h2 class="about-head" style="top:312px">Leadership commitments</h2>
    <div class="about-photo photo warm left" role="img" aria-label="Photo of crew on a lift working on aluminum bus in a substation"></div>
  </section>

  <!-- Panel 2 -->
  <section class="panel about">
    <div class="about-row" style="top:0;height:110px"></div>
    <div class="about-row" style="top:110px;height:80px"></div>
    <div class="about-row" style="top:190px;height:40px"></div>
    <div class="about-row" style="top:230px;height:32px"></div>
    <div class="about-row" style="top:262px;height:40px"></div>
    <div class="about-row" style="top:302px;height:120px"></div>
    <p class="about-body" style="top:16px">Brevo Forge &amp; Fabrication, Inc. is dedicated to delivering quality craftsmanship without compromise. For over three decades our crews have welded aluminum bus for utilities and contractors across the region. We continue to grow by holding ourselves to the highest standards and treating every project as a long term partnership.</p>
    <p class="about-body" style="top:116px"><b>Safety</b> – every task is planned so each person goes home safe. <b>Integrity</b> – we do what we say. <b>Innovation</b> – finding better ways to build. <b>Respect</b> – valuing our people and clients. <b>Teamwork</b> – working together to deliver.</p>
    <p class="about-body" style="top:196px">Our skilled welders and field crews are certified, experienced and trained to meet the demands of every substation.</p>
    <p class="about-body" style="top:238px">Licensed to perform work in multiple states across the country.</p>
    <p class="about-body" style="top:268px">Registered with leading safety networks so your approval process stays fast and simple.</p>
    <div class="about-body" style="top:310px">
      <ul>
        <li>Accountability and ownership of every product</li>
        <li>Exceptional quality in every weld, every time</li>
        <li>Investing in training, tools and our people</li>
        <li>Clear communication from bid to final walk</li>
        <li>Continuous improvement of safety practices</li>
      </ul>
      <p style="margin-top:4px">Brevo Forge is a proud member of multiple trade associations and holds current industry certifications.</p>
    </div>
    <div class="about-photo photo warm right" role="img" aria-label="Photo of substation structure with insulators and welded bus"></div>
    <div class="fade"></div>
    <div class="badges" aria-label="Association memberships">
      <span class="badge rect"></span><span class="badge rect"></span><span class="badge rect"></span><span class="badge round"></span>
    </div>
  </section>

  <!-- Panel 3 -->
  <section class="panel services services-left">
    <div class="edge"></div>
    <h1 class="svc-title"><span class="small">SERVICE</span><span class="big">PROVIDED</span></h1>
    <p class="svc-sub">Specialty aluminum welding services that bring quality, speed and value to every substation project.</p>
    <div class="dash" style="top:150px"></div>

    <article class="card red" style="top:172px;height:215px">
      <div class="copy">
        <h3>All Weather Welding</h3>
        <p>Our crews keep projects moving through rain, snow and wind using enclosures and heating so schedules stay on track.</p>
        <h4>Types of weather we successfully perform quality welds in</h4>
        <ul><li>Rain</li><li>Snow</li><li>Wind</li><li>Extreme heat and cold</li></ul>
        <h4>Advantage</h4>
        <p>No lost days waiting on the weather and safe, consistent welds in all conditions.</p>
      </div>
      <span class="notch" style="top:150px"></span>
    </article>
    <div class="pcol">
      <div class="photo" role="img" aria-label="Photo of welded bus structure" style="left:186px;top:176px"></div>
      <div class="photo sky" role="img" aria-label="Photo of weld truck at substation in winter" style="left:186px;top:240px"></div>
      <div class="photo sky" role="img" aria-label="Photo of crews welding at a substation" style="left:186px;top:304px"></div>
    </div>

    <article class="card teal" style="top:410px;height:215px">
      <div class="copy">
        <h3>Bus Bending</h3>
        <p>We bend rigid aluminum bus in the shop or the field to match your design, reducing the number of fittings and joints needed.</p>
        <h4>What we do</h4>
        <p>Precise bends on pipe and tube bus with calibrated tools and full dimensional checks.</p>
        <h4>Advantage</h4>
        <p>Fewer fittings, lower material cost, cleaner appearance and less chance of joint failure.</p>
      </div>
      <span class="notch" style="top:150px"></span>
    </article>
    <div class="pcol">
      <div class="photo sky" role="img" aria-label="Photo of bent aluminum bus" style="left:186px;top:414px"></div>
      <div class="photo" role="img" aria-label="Photo of substation bus layout" style="left:186px;top:478px"></div>
      <div class="photo sky" role="img" aria-label="Photo of bus bending in the field" style="left:186px;top:542px"></div>
    </div>
  </section>

  <!-- Panel 4 -->
  <section class="panel services">
    <div class="field-list">
      <h5>Field Services:</h5>
      <p>Fully equipped mobile welding units. Certified aluminum welders. Welding at your construction site.</p>
      <h5>Shop Services:</h5>
      <p>Prefabrication and welding of bus assemblies in our fully equipped facility.</p>
      <h5>All Weather Services:</h5>
      <p>Built in the field with shelters and heat, we weld through any season. <b>24 hour availability / 7 days a week</b></p>
    </div>
    <div class="dash" style="top:160px"></div>

    <article class="card teal" style="top:182px;height:215px">
      <div class="copy">
        <h3>Aluminum Welding</h3>
        <p>Welded connections create a continuous conductor with lower resistance and no hardware to loosen over time.</p>
        <h4>What we do</h4>
        <p>Welding of pipe bus, tube bus, fittings, couplers and terminal pads on new and existing substations.</p>
        <h4>Advantage</h4>
        <p>Long lasting connections, lower maintenance and a clean, strong finished structure.</p>
      </div>
      <span class="notch" style="top:155px"></span>
    </article>
    <div class="pcol">
      <div class="photo sky" role="img" aria-label="Photo of welder at work" style="left:186px;top:190px"></div>
      <div class="photo warm" role="img" aria-label="Photo of crew on lift welding bus" style="left:186px;top:254px"></div>
      <div class="photo" role="img" aria-label="Photo of welded aluminum fittings" style="left:186px;top:318px"></div>
    </div>

    <article class="card red" style="top:428px;height:220px">
      <div class="copy">
        <h3>Field Fabrication</h3>
        <p>When drawings change on site, our crews cut, fit and weld new assemblies right where they are needed.</p>
        <h4>What we do</h4>
        <p>Custom supports, bus extensions, jumpers and modifications built to match field conditions.</p>
        <h4>Advantage</h4>
        <p>Avoid costly delays and return trips while keeping your project moving forward to completion.</p>
      </div>
      <span class="notch" style="top:160px"></span>
    </article>
    <div class="pcol">
      <div class="photo" role="img" aria-label="Photo of fabricated aluminum tube" style="left:186px;top:436px"></div>
      <div class="photo sky" role="img" aria-label="Photo of substation with welded bus" style="left:186px;top:500px"></div>
      <div class="photo" role="img" aria-label="Photo of field fabricated assembly" style="left:186px;top:564px"></div>
    </div>
    <div class="dash" style="top:690px"></div>
  </section>

</div>
</body>
</html>
```